Ashcombe Field Surveyors Business Card

We are a land surveying company looking for a business card with a clean, sharp design. We would like for our design to portray our logo on one side, and contact information on the other w/ or w/o logo. Our colors preferred are navy blue, grey/silver, white and black. thank you!

Industry/Entity Type

Surveyor

Contact Information for Business Card

Ashcombe Field Surveyors
Dorian Kavatsky, P.L.S.
(555) 302-4619
Ashcombefieldsurveyors@ashmail-example.net
Ashcombefieldsurveyors-example.com
287 Linden Terrace, Ashcombe MA 01999

Requirements
Must have
• 1. Company Name
2. Personal name and title
3. phone number
4. email.
5. website
6. address

```html
<!DOCTYPE html>
<html lang="en">
<head>
<meta charset="utf-8">
<title>Ashcombe Field Surveyors – Business Card</title>
<link rel="stylesheet" href="https://fonts.googleapis.com/css2?family=Poppins:wght@400;500;700&display=swap">
<style>
  :root {
    --navy: #2f3690;
    --white: #ffffff;
    --ink: #2b2b2b;
    --stage: #1c1c1e;
    --rule: #3a40a0;
  }
  * { box-sizing: border-box; margin: 0; padding: 0; }
  html, body {
    width: 1200px; height: 1200px; overflow: hidden;
    background: var(--stage);
    font-family: "Poppins", sans-serif;
  }
  .sheet {
    width: 1200px; height: 1200px;
    display: flex; flex-direction: column; align-items: center; justify-content: center;
    gap: 44px;
  }
  .card {
    width: 900px; height: 514px;
    position: relative;
    box-shadow: 0 12px 30px rgba(0,0,0,0.5);
  }
  .card-front {
    background: var(--navy);
    display: flex; align-items: center; justify-content: center;
  }
  .brand {
    display: flex; align-items: center; gap: 18px;
    font-weight: 700; letter-spacing: 0.06em; line-height: 1.1;
  }
  .brand-name { text-transform: uppercase; }
  .brand-dot {
    width: 30px; height: 30px; border-radius: 50%; flex: none;
  }
  .card-front .brand { color: var(--white); font-size: 42px; }
  .card-front .brand-dot { background: var(--white); }
  .card-back {
    background: var(--white);
    display: flex; align-items: center;
  }
  .back-brand {
    width: 400px; padding-left: 40px; padding-right: 24px;
    display: flex; justify-content: center;
  }
  .card-back .brand { color: var(--navy); font-size: 30px; gap: 14px; }
  .card-back .brand-dot { background: var(--navy); width: 22px; height: 22px; }
  .divider {
    width: 2px; height: 230px; background: var(--rule); flex: none;
  }
  .contact {
    padding-left: 30px; padding-right: 20px; color: var(--ink);
  }
  .contact-name {
    color: var(--navy); font-weight: 700; font-size: 27px; line-height: 1.15;
  }
  .contact-title { font-size: 18px; margin-bottom: 16px; }
  .contact-address { font-size: 18px; line-height: 1.3; margin-bottom: 12px; }
  .contact-line {
    display: flex; align-items: center; gap: 9px;
    font-size: 17px; line-height: 1.55; white-space: nowrap;
  }
  .contact-line.email { font-size: 16px; }
  .contact-icon { width: 16px; height: 16px; flex: none; fill: var(--navy); }
</style>
</head>
<body>
<main class="sheet">
  <section class="card card-front">
    <div class="brand"><span class="brand-dot"></span><span class="brand-name">Ashcombe<br>Field Surveyors</span></div>
  </section>

  <section class="card card-back">
    <div class="back-brand">
      <div class="brand"><span class="brand-dot"></span><span class="brand-name">Ashcombe<br>Field Surveyors</span></div>
    </div>
    <div class="divider"></div>
    <div class="contact">
      <p class="contact-name">Dorian Kavatsky, P.L.S.</p>
      <p class="contact-title">Manager</p>
      <p class="contact-address">287 Linden Terrace<br>Ashcombe MA 01999</p>
      <p class="contact-line phone">
        <svg class="contact-icon" viewBox="0 0 16 16" aria-hidden="true"><path d="M4 1h3l1 4-2 1.2c.8 1.7 2 2.9 3.8 3.8L11 8l4 1v3c0 1-1 2-2 2C7 14 2 9 2 3c0-1 1-2 2-2z"/></svg>
        (555) 302-4619
      </p>
      <p class="contact-line email">
        <svg class="contact-icon" viewBox="0 0 16 16" aria-hidden="true"><path d="M1 3h14v10H1z M2 4l6 5 6-5" fill="none" stroke="#2f3690" stroke-width="1.6"/></svg>
        Ashcombefieldsurveyors@ashmail-example.net
      </p>
      <p class="contact-line">
        <svg class="contact-icon" viewBox="0 0 16 16" aria-hidden="true"><g fill="none" stroke="#2f3690" stroke-width="1.3"><circle cx="8" cy="8" r="6.5"/><ellipse cx="8" cy="8" rx="3" ry="6.5"/><path d="M1.5 8h13M2.5 4.8h11M2.5 11.2h11"/></g></svg>
        Ashcombefieldsurveyors-example.com
      </p>
    </div>
  </section>
</main>
</body>
</html>
```